Training flyer for 1/2 day modules

We need a flyer to be designed for some training sessions. It needs to be professional for the defence industry. It also needs to be able to be completed online - with tick boxes etc. Should be A4 back to back. Included in the documents below is some samples of previous brochures that we have had. Also below are some reviews from previous training - please use these somewhere;

- Great training, best I've ever had on this topic.
- Great presenter - very knowledgable.
- Course was very well presented and organised.

PLEASE USE MODULE TRAINING MOCK-UP FLYER ATTACHED FILE FOR CONTENT.

Target Market(s)

Defence industry

Industry/Entity Type

Defence

Requirements
Must have
• professional look - be able to be completed online,

```html
<!DOCTYPE html>
<html lang="en">
<head>
<meta charset="utf-8">
<title>Advanced Defence, EAR &amp; ITAR Half-Day Training Modules</title>
<link rel="stylesheet" href="https://fonts.googleapis.com/css2?family=Black+Ops+One&family=Righteous&family=Roboto:ital,wght@0,400;0,500;0,700;1,400&family=Tinos:ital,wght@0,400;0,700;1,400&display=swap">
<style>
  :root {
    --stage: #2e2e2e;
    --paper: #ffffff;
    --green: #3f9a3a;
    --green-dark: #2d7a2b;
    --green-light: #7cc043;
    --row-tint: #dcebd9;
    --yellow: #f4e01c;
    --ink: #2b2b2b;
    --ink-soft: #4a4a4a;
    --photo-a: #5f7a4a;
    --photo-b: #a8b98c;
    --scene-a: #cfd4cc;
    --scene-b: #eef0ec;
  }
  * { box-sizing: border-box; margin: 0; padding: 0; }
  html, body { width: 1200px; height: 900px; overflow: hidden; background: var(--stage); }
  .canvas { position: relative; width: 1200px; height: 900px; }
  .sheet { position: absolute; top: 135px; width: 478px; height: 630px; background: var(--paper); overflow: hidden; font-family: "Roboto", sans-serif; color: var(--ink); }
  .sheet--front { left: 102px; }
  .sheet--back { left: 618px; }
  .abs { position: absolute; }

  /* tick box */
  .tick { appearance: none; -webkit-appearance: none; width: 10px; height: 10px; border: 1px solid var(--ink); background: #fff; vertical-align: -1px; margin-right: 4px; }
  .tick:checked { background: var(--green); border-color: var(--green); }

  /* front */
  .hero { left: 0; top: 0; width: 478px; height: 320px; }
  .lower-scene { left: 0; top: 420px; width: 478px; height: 185px; background: linear-gradient(180deg, var(--paper), var(--scene-a) 60%, var(--scene-b)); opacity: .55; }
  .headline { left: 30px; top: 212px; font-family: "Black Ops One", sans-serif; font-size: 62px; line-height: 1; color: var(--green-light); letter-spacing: 1px; }
  .ribbon { left: 28px; top: 289px; width: 230px; height: 22px; background: var(--yellow); font-weight: 700; font-size: 11.5px; line-height: 22px; padding-left: 10px; color: var(--ink); }
  .brand { display: flex; align-items: center; gap: 10px; }
  .brand__mark { width: 44px; height: 44px; border-radius: 50%; background: var(--green); flex: none; }
  .brand__name { font-weight: 500; color: var(--green); line-height: 1.05; }
  .front-brand { left: 28px; top: 332px; }
  .front-brand .brand__mark { width: 80px; height: 80px; }
  .front-brand .brand__name { font-size: 18px; width: 120px; }
  .course-title { left: 264px; top: 339px; font-family: "Righteous", sans-serif; font-size: 18px; color: var(--green); letter-spacing: .5px; white-space: nowrap; }
  .course-dates { left: 264px; top: 362px; font-size: 12.5px; line-height: 20px; color: var(--ink); }
  .course-dates b { font-weight: 700; }
  .program { left: 264px; top: 403px; font-size: 30px; font-weight: 400; color: var(--ink); }
  .program-time { left: 266px; top: 440px; font-size: 14px; font-weight: 700; color: var(--green); }
  .program-time span { color: var(--ink); font-weight: 400; }
  .program-time small { font-size: 12px; color: var(--ink); font-weight: 400; }
  .audience-band { left: 0; top: 428px; width: 214px; height: 28px; background: var(--green); clip-path: polygon(0 0, 100% 0, 93% 100%, 0 100%); color: #fff; font-weight: 700; font-size: 16px; line-height: 28px; padding-left: 27px; }
  .audience-text { left: 24px; top: 466px; width: 182px; font-size: 8.6px; line-height: 10.4px; color: var(--ink-soft); text-align: justify; }
  .guest-box { left: 22px; top: 537px; width: 184px; height: 58px; background: var(--green); border: 2px solid #fff; border-radius: 8px; box-shadow: 0 0 0 1px var(--green); color: #fff; font-weight: 700; font-size: 12.5px; line-height: 15px; text-align: center; padding-top: 6px; }
  .about-text { left: 214px; top: 466px; width: 254px; font-size: 8.6px; line-height: 10.4px; color: var(--ink-soft); text-align: justify; }
  .contact-bar { left: 0; top: 605px; width: 478px; height: 25px; background: var(--green); display: flex; align-items: center; color: #fff; font-size: 10.5px; }
  .contact-bar__item { display: flex; align-items: center; gap: 6px; padding: 0 16px; border-right: 1px solid rgba(255,255,255,.6); }
  .contact-bar__item:last-child { border-right: 0; }
  .contact-bar svg { width: 11px; height: 11px; fill: #fff; }

  /* back */
  .back-brand { left: 22px; top: 10px; }
  .back-brand .brand__mark { width: 36px; height: 36px; }
  .back-brand .brand__name { font-size: 12px; width: 96px; }
  .location { right: 22px; top: 28px; font-family: "Tinos", serif; text-align: right; }
  .location h3 { font-size: 13px; font-weight: 700; padding-right: 60px; }
  .location__options { display: flex; gap: 10px; font-size: 9.5px; font-weight: 700; margin-top: 5px; }
  .location__options label { display: flex; align-items: center; }
  .register-title { left: 20px; top: 80px; font-family: "Tinos", serif; font-weight: 700; font-size: 21px; color: var(--green); }
  .form { left: 20px; top: 110px; width: 438px; font-family: "Tinos", serif; font-size: 10.5px; color: var(--ink); }
  .field { height: 15px; background: var(--row-tint); padding-left: 3px; line-height: 15px; margin-bottom: 2px; }
  .field-group { margin-bottom: 9px; }
  .field-block { background: var(--row-tint); padding: 3px; line-height: 14px; height: 46px; margin-bottom: 6px; }
  .pay-row { background: var(--row-tint); height: 30px; display: flex; align-items: center; padding-left: 3px; margin-bottom: 12px; }
  .pay-row b { font-size: 8.5px; width: 160px; }
  .pay-row label { font-size: 12px; width: 135px; display: flex; align-items: center; }
  .card-rows .field { margin-bottom: 2px; background: rgba(220,235,217,.85); }
  .back-scene { left: 0; top: 455px; width: 478px; height: 90px; background: linear-gradient(180deg, var(--paper), var(--scene-a) 55%, var(--scene-b)); opacity: .6; }
  .reviews { left: 20px; top: 470px; width: 438px; font-family: "Tinos", serif; }
  .reviews h3 { font-size: 11px; font-weight: 700; color: var(--green); margin-bottom: 3px; letter-spacing: .3px; }
  .reviews p { font-size: 10px; line-height: 13px; font-style: italic; color: var(--ink); }
  .badges { left: 0; top: 540px; width: 478px; height: 80px; background: var(--paper); display: flex; align-items: center; justify-content: space-around; padding: 0 18px; }
  .badge-divider { width: 1px; height: 58px; background: #bdbdbd; }
  .badge--round { width: 64px; height: 64px; border-radius: 50%; background: #1f3b6e; }
  .badge--crest { width: 94px; height: 50px; background: #c9c9c9; }
  .badge--seal { width: 60px; height: 60px; border-radius: 50%; background: #d8d8d8; }
  .badge--square { width: 76px; height: 56px; background: #3c7bbf; }
  .back-foot { left: 0; top: 620px; width: 478px; height: 10px; background: #8d8d8d; }
</style>
</head>
<body>
<div class="canvas">

  <section class="sheet sheet--front">
    <svg class="abs hero" viewBox="0 0 478 320" role="img" aria-label="Photograph of soldiers in camouflage gear and helmets aiming rifles">
      <defs>
        <linearGradient id="heroTone" x1="0" y1="0" x2="1" y2="1">
          <stop offset="0" stop-color="#a8b98c"/>
          <stop offset=".55" stop-color="#5f7a4a"/>
          <stop offset="1" stop-color="#8a8f6a"/>
        </linearGradient>
      </defs>
      <path d="M0 0 H478 V250 C380 300 200 330 0 300 Z" fill="url(#heroTone)"/>
      <path d="M0 0 C4 90 18 150 30 180 L0 180 Z" fill="#ffffff"/>
      <path d="M0 303 C200 333 380 303 478 250 L478 268 C380 318 200 345 0 318 Z" fill="#3f9a3a"/>
      <path d="M0 318 C200 345 380 318 478 268 L478 320 L0 320 Z" fill="#ffffff"/>
    </svg>

    <div class="abs lower-scene" role="img" aria-label="Faded photograph of a military tank"></div>

    <h1 class="abs headline">ADVANCED</h1>
    <div class="abs ribbon">DEFENCE,EAR,&amp;ITAR TRANING</div>

    <div class="abs brand front-brand">
      <span class="brand__mark"></span>
      <span class="brand__name">Northgate Trade Compliance Institute</span>
    </div>

    <h2 class="abs course-title">1/2 DAY MODULES</h2>
    <p class="abs course-dates"><b>Sydney</b> - 19,20,21 October<br><b>Canberra</b> - 22,23,26 October</p>
    <h2 class="abs program">Program</h2>
    <p class="abs program-time">09:00 <span>to</span> 12:30 <small>Each Module</small></p>

    <div class="abs audience-band">Who should attend:</div>
    <p class="abs audience-text">Practitioners that work for companies that deal with U.S. based technology or that purchase U.S origin products, components or technology. The Advanced modules assume a basic understand of U.S. trade controls.</p>
    <div class="abs guest-box">Guest presenters will<br>Deliver different aspects<br>Of the traning program</div>

    <p class="abs about-text">U.S. Export Controls are some of the most complex and stringent in the world. The U.S. Government regulates the transfer of U.S. origin goods and technical data throughout the world, with the intent of preventing unauthorised transfer of technology and know-how. These controls extend world-wide and can impact anyone dealing in U.S. controlled goods or technology. These half-day advanced modules are designed to give attendees a greater understanding of U.S. Export Controls from a non-U.S. perspective in practical and relevant terms. Though we will cover a lot of material the modules are designed for practitioners with an existing knowledge.</p>

    <div class="abs contact-bar">
      <span class="contact-bar__item"><svg viewBox="0 0 24 24"><path d="M6.6 10.8a15 15 0 0 0 6.6 6.6l2.2-2.2c.3-.3.7-.4 1-.2 1.1.4 2.3.6 3.6.6.6 0 1 .4 1 1V20c0 .6-.4 1-1 1A17 17 0 0 1 3 4c0-.6.4-1 1-1h3.5c.6 0 1 .4 1 1 0 1.2.2 2.4.6 3.6.1.3 0 .7-.2 1z"/></svg>+61 (0)7 5550 1234</span>
      <span class="contact-bar__item"><svg viewBox="0 0 24 24"><path d="M12 2a10 10 0 1 0 0 20 10 10 0 0 0 0-20zm0 2c.8 1.2 1.5 2.5 1.9 4h-3.8c.4-1.5 1.1-2.8 1.9-4zM4.3 14a8 8 0 0 1 0-4h3.4a16 16 0 0 0 0 4zm7.7 6c-.8-1.2-1.5-2.5-1.9-4h3.8c-.4 1.5-1.1 2.8-1.9 4zm2.3-6H9.7a14 14 0 0 1 0-4h4.6a14 14 0 0 1 0 4zm2 0a16 16 0 0 0 0-4h3.4a8 8 0 0 1 0 4z"/></svg>www.northgatetci.com</span>
      <span class="contact-bar__item"><svg viewBox="0 0 24 24"><path d="M2 5h20v14H2zm2 2v.5l8 5 8-5V7zm0 2.8V17h16V9.8l-8 5z"/></svg>info@northgatetci.com</span>
    </div>
  </section>

  <section class="sheet sheet--back">
    <div class="abs back-scene" role="img" aria-label="Faded photograph of a military tank"></div>

    <div class="abs brand back-brand">
      <span class="brand__mark"></span>
      <span class="brand__name">Northgate Trade Compliance Institute</span>
    </div>

    <div class="abs location">
      <h3>LOCATION:</h3>
      <div class="location__options">
        <label><input class="tick" type="checkbox" name="location" value="sydney">Sydney</label>
        <label><input class="tick" type="checkbox" name="location" value="canberra">Canberra</label>
        <label><input class="tick" type="checkbox" name="location" value="brisbane">Brisbane</label>
      </div>
    </div>

    <h2 class="abs register-title">HOW TO REGISTER:</h2>

    <form class="abs form">
      <div class="field-group"><div class="field">Attendee name:</div><div class="field">Email:</div></div>
      <div class="field-group"><div class="field">Attendee name:</div><div class="field">Email:</div></div>
      <div class="field-group"><div class="field">Attendee name:</div><div class="field">Email:</div></div>
      <div class="field-group"><div class="field">Attendee name:</div><div class="field">Email:</div></div>
      <div class="field-block">Company:<br>Email:<br>Phone:</div>
      <div class="pay-row">
        <b>PAYMENT METHOD:</b>
        <label><input class="tick" type="checkbox" name="payment" value="invoice">Invoice</label>
        <label><input class="tick" type="checkbox" name="payment" value="card">credit card</label>
      </div>
      <div class="card-rows">
        <div class="field">Credit card number:</div>
        <div class="field">Card name:</div>
        <div class="field">Expiry date:</div>
        <div class="field">CVV</div>
        <div class="field">Card holder email:</div>
      </div>
    </form>

    <div class="abs reviews">
      <h3>WHAT ATTENDEES SAY:</h3>
      <p>“Great training, best I've ever had on this topic.”</p>
      <p>“Great presenter - very knowledgable.”</p>
      <p>“Course was very well presented and organised.”</p>
    </div>

    <div class="abs badges">
      <span class="badge--round"></span>
      <span class="badge-divider"></span>
      <span class="badge--crest"></span>
      <span class="badge-divider"></span>
      <span class="badge--seal"></span>
      <span class="badge-divider"></span>
      <span class="badge--square"></span>
    </div>
    <div class="abs back-foot"></div>
  </section>

</div>
</body>
</html>
```